Golden Coat All-Purpose Breading Bag Design

Our client, Harlow Food Products, is looking to re-design the packaging for their product, Pellworth's Golden Coat. Goldn Coat is an all-purpose food breading mix.

Harlow Foods has a registered trademark for this product, but they have not been using it for this particular 10 pound bag. They want to get the trademark onto the bag and also give the bag an updated look. They would like to continue to use the same red and blue colors. This 10 pound bag is not available on store shelves; it is sold to food service distributors who sell to restaurants.

All of the copy on the existing bag is still relevant, so we will want to incoprporate it into the bag design. Once these bags are filled with product, the tops get folded over about 1 inch and then sewn shut with thread.

Eventually, we will need the design applied to the Bag Template file attached, but that isn't important until a design is selected.

Target Market(s)

Restaurants

Industry/Entity Type

Food Manufacturing

Colors
0054AA
0677BA
7BADD7
CADEEF
E8F1F8
EB3D1F
EC4F4E
F09395
F8D3D4
FCEDEE

Requirements
Must have
• Trademark introduced to the design

```html
<!DOCTYPE html>
<html lang="en">
<head>
<meta charset="utf-8">
<title>Pellworth's Golden Coat – Breading Bag</title>
<link rel="stylesheet" href="https://fonts.googleapis.com/css2?family=Barlow:wght@300;400;600;700&family=Kaushan+Script&family=Poppins:wght@600;700&display=swap">
<style>
  :root {
    --page: #ffffff;
    --navy: #0b1786;
    --blue-mid: #1a55ad;
    --blue-light: #2279c0;
    --red: #991409;
    --red-band: #a72d24;
    --white: #ffffff;
    --ink: #2a2a2a;
  }
  html, body {
    margin: 0;
    padding: 0;
    width: 1136px;
    height: 1200px;
    overflow: hidden;
    background: var(--page);
  }
  .canvas {
    position: relative;
    width: 1136px;
    height: 1200px;
  }
  .bag {
    position: absolute;
    left: 273px;
    top: 71px;
    width: 589px;
    height: 1054px;
    overflow: hidden;
    color: var(--white);
  }
  .bag-art {
    position: absolute;
    inset: 0;
    width: 100%;
    height: 100%;
  }
  .claim-band {
    position: absolute;
    left: 0;
    top: 591px;
    width: 100%;
    height: 139px;
    background: var(--red-band);
  }
  .brand-name {
    position: absolute;
    left: 54px;
    top: 160px;
    font-family: "Poppins", sans-serif;
    font-weight: 600;
    font-size: 46px;
    line-height: 1;
    letter-spacing: 0.5px;
  }
  .cook-time {
    position: absolute;
    left: 392px;
    top: 163px;
    width: 170px;
    height: 121px;
    background: var(--white);
    border-radius: 0 0 8px 8px;
    text-align: center;
    color: var(--ink);
    box-shadow: inset 0 12px 10px -8px rgba(0,0,0,0.25);
  }
  .cook-time svg {
    display: block;
    margin: 22px auto 0;
  }
  .cook-time p {
    margin: 10px 0 0;
    font-family: "Barlow", sans-serif;
    font-weight: 300;
    font-size: 13px;
    line-height: 14px;
    letter-spacing: -0.4px;
  }
  .product-owner {
    position: absolute;
    left: 0;
    width: 100%;
    top: 330px;
    text-align: center;
    font-family: "Kaushan Script", cursive;
    font-size: 78px;
    line-height: 1;
    transform: rotate(-4deg);
  }
  .product-name {
    position: absolute;
    left: 0;
    width: 100%;
    top: 420px;
    text-align: center;
    font-family: "Poppins", sans-serif;
    font-weight: 700;
    font-size: 84px;
    line-height: 1.2;
    letter-spacing: -3.5px;
  }
  .claim {
    position: absolute;
    left: 54px;
    top: 620px;
    font-family: "Barlow", sans-serif;
  }
  .claim h2 {
    margin: 0;
    font-weight: 700;
    font-size: 29px;
    line-height: 32px;
    letter-spacing: 0.5px;
  }
  .claim p {
    margin: 6px 0 0;
    font-weight: 400;
    font-size: 19px;
    line-height: 19px;
    letter-spacing: 0.3px;
  }
  .net-weight {
    position: absolute;
    right: 26px;
    top: 770px;
    font-family: "Barlow", sans-serif;
    font-size: 35px;
    line-height: 36px;
    font-weight: 400;
    letter-spacing: 0.5px;
  }
  .net-weight strong { font-weight: 700; }
  .rule {
    position: absolute;
    left: 165px;
    top: 809px;
    width: 395px;
    height: 3px;
    background: var(--white);
  }
  .ingredients {
    position: absolute;
    right: 26px;
    top: 817px;
    margin: 0;
    text-align: right;
    font-family: "Barlow", sans-serif;
    font-size: 14.5px;
    line-height: 16px;
    letter-spacing: 0.3px;
    text-transform: uppercase;
  }
  .ingredients strong { font-weight: 700; }
</style>
</head>
<body>
<div class="canvas">
  <div class="bag">
    <svg class="bag-art" viewBox="0 0 972 1757" preserveAspectRatio="none" aria-hidden="true">
      <defs>
        <linearGradient id="blueSweep" x1="0" y1="0" x2="1" y2="0">
          <stop offset="0" stop-color="#0b1786"/>
          <stop offset="0.35" stop-color="#1a63b8"/>
          <stop offset="0.62" stop-color="#2279c0"/>
          <stop offset="0.85" stop-color="#1549a6"/>
          <stop offset="1" stop-color="#0b1786"/>
        </linearGradient>
        <linearGradient id="waveShade" x1="0" y1="0" x2="0" y2="1">
          <stop offset="0" stop-color="#000" stop-opacity="0.4"/>
          <stop offset="1" stop-color="#000" stop-opacity="0"/>
        </linearGradient>
      </defs>
      <rect width="972" height="1757" fill="#991409"/>
      <path d="M0,195 C200,177 420,198 620,241 S860,282 972,262 L972,292 C860,312 620,271 420,228 S200,207 0,225 Z" fill="url(#waveShade)"/>
      <path d="M0,0 H972 V256 C860,278 620,238 420,196 S200,175 0,192 Z" fill="url(#blueSweep)"/>
      <path d="M0,195 C200,177 420,198 620,241 S860,282 972,262" fill="none" stroke="#fff" stroke-width="9"/>
      <path d="M0,1432 C200,1402 420,1428 620,1472 S860,1520 972,1497 V1757 H0 Z" fill="url(#blueSweep)"/>
      <path d="M0,1427 C200,1397 420,1423 620,1467 S860,1515 972,1492" fill="none" stroke="#fff" stroke-width="9"/>
    </svg>

    <div class="claim-band"></div>

    <div class="brand-name">Harlow</div>

    <div class="cook-time">
      <svg width="40" height="40" viewBox="0 0 40 40" aria-hidden="true">
        <circle cx="20" cy="20" r="17" fill="none" stroke="#991409" stroke-width="4"/>
        <path d="M18 10 V22 H27" fill="none" stroke="#991409" stroke-width="4" stroke-linecap="round" stroke-linejoin="round"/>
      </svg>
      <p>Cooks two-pound chicken<br>well done in 10 min.</p>
    </div>

    <div class="product-owner">Pellworth's</div>
    <div class="product-name">GoldenCoat</div>

    <div class="claim">
      <h2>SEALS JUICE IN-GREASE OUT</h2>
      <p>Chicken fried the GOLDEN COAT way<br>is fried chicken the right away.</p>
    </div>

    <div class="net-weight"><strong>NET WT.</strong> 10 LBS.</div>
    <div class="rule"></div>
    <p class="ingredients"><strong>Ingredients:</strong> Flour, salt, eggs yolk,<br>non-fat milk solids, baking powder,<br>corn starch, sugar and pepper.</p>
  </div>
</div>
</body>
</html>
```